Pamphlet Days of the Family - École Mont-Clairval

We * need a pamphlet (flyer) to describe a new project. This project is called "Family Days - École Mont-Clairval". The text describing family days and their intended goals is attached in the downloaded .doc document. We also provided the logo (LE JOURNESS no font in attachment) which represents the school and those days of the family. Please write "Family Days - École Mont-Clairval" on top of the pamphlet with the Logo in plain view (The text The days of the École Mont-Clairval family must be associated with the logo). We need the pamphlet to be colorful, attractive and clean as much as possible. We would like to have childish drawings (see drawing example attached) and photos that represent one or both parents with their child (ren) in a SCHOOL ENVIRONMENT (very important). Parents must feel concerned. It can be a two-sided pamphlet. In color (bright colors as much as possible). The text must be in French so only FRENCH DESIGNERS ARE INVITED to work on this design because the text must remain consistent. The project can be summed up as follows: The Mont-Clairval School wishes to open its doors so that parents can share with their child moments in their student life. They will be invited, at various times of the school year, to participate in the daily life of their child, for example ... • during special activities in class (eg reading, do-it-yourself, job presentation, etc.). events (eg, back to school, Christmas choir, carnival, etc.) • during educational and sports outings (eg skating, library, cinema, etc.) Also, they will have the opportunity to come and spend a period in their child's classroom. They will have the privilege of accompanying him during a usual learning moment. For any additional question, thank you to contact me via this page, it will be my pleasure to answer you quickly. Thank you all for your participation. * We are a committee made up of parents, teachers, school principal, school administrators. Everyone has a say in the final design. So I am only the intermediary responsible for the project. It will be my pleasure to share with you the information received from these different partners for this project.

Target Market(s)

Parents of students at a primary school (ages 5 to 12).

Font styles to use
Sans Serif

Colors

Designer to choose colors to be used in the design.

Requirements
Must have
• The Logo prominently Pamphlet Colorful (beautiful bright colors) Easy to read and understand (some parents speak very little French) Originality (Attractive) Text In French (required) and consistent
Nice to have
• One or more Childish Drawing (s) One (1) parent-child Photo (s) in a school environment Allure Épuré
Should not have
• The Dark Colors Of the Scriptures Too Small A Condensed Text Text English

```html
<!DOCTYPE html>
<html lang="fr">
<head>
<meta charset="utf-8">
<title>Les journées de la famille de Mont-Clairval</title>
<link rel="stylesheet" href="https://fonts.googleapis.com/css2?family=Raleway:wght@300;400;500;600;700&display=swap">
<style>
  :root{
    --bg:#e9e9e9;
    --paper:#ffffff;
    --sun:#f7c21b;
    --sun-soft:#fde9a0;
    --ink:#1b1b1b;
    --title:#e2173a;
    --kid-orange:#f0925f;
    --node-red:#e8606a;
    --node-orange:#e7704e;
    --school-green:#8ba54a;
    --teacher-orange:#f2a43c;
    --parent-lilac:#a3a7d6;
    --chalk:#ffffff;
  }
  *{box-sizing:border-box;margin:0;padding:0}
  html,body{width:1200px;height:953px;overflow:hidden;background:var(--bg)}
  body{font-family:"Raleway",sans-serif;color:var(--ink);position:relative}
  .flyer{position:absolute;left:0;top:52px;width:1200px;height:848px;background:var(--paper);overflow:hidden}
  .panel{position:absolute;left:28px;top:36px;width:1144px;height:773px;border-radius:40px;
    background:linear-gradient(90deg,var(--sun) 0%,#f9d04a 25%,var(--sun-soft) 55%,#fff6dc 80%,#ffffff 100%)}
  .photo{position:absolute;left:782px;top:36px;width:390px;height:456px;border-radius:0 40px 40px 0;
    background:linear-gradient(160deg,#dfe4ea 0%,#c9ccd3 35%,#9aa4c1 70%,#4d63b0 100%);
    -webkit-mask-image:linear-gradient(90deg,transparent 0%,#000 22%);mask-image:linear-gradient(90deg,transparent 0%,#000 22%)}
  .diagram{position:absolute;left:0;top:0;width:1200px;height:848px;z-index:1}
  .kid{position:absolute;border-radius:50% 50% 10px 10px;opacity:.8;z-index:2}
  .kid--left{left:0;top:625px;width:112px;height:223px;background:linear-gradient(180deg,#fff 0%,#7fa64a 45%,#5a4a7a 100%)}
  .kid--flower{left:440px;top:742px;width:184px;height:106px;background:linear-gradient(180deg,#fff 0%,#e8d96a 60%,#f2e03c 100%)}
  .kid--red{left:690px;top:700px;width:160px;height:148px;background:linear-gradient(180deg,#e45a3a 0%,#e8303a 60%,#d8243a 100%)}
  .kid--right{left:1122px;top:696px;width:78px;height:152px;background:linear-gradient(180deg,#fff 0%,#5cc0d6 60%,#6a56a8 100%)}
  .intro,.bubble,.node,.title{z-index:3}
  .intro{position:absolute;left:66px;top:92px;width:360px;font-size:14px;line-height:20.5px;font-weight:400;white-space:nowrap}
  .intro p.lead{font-weight:500;margin-bottom:9px}
  .intro ul{list-style:none;margin-bottom:6px}
  .intro li{position:relative;padding-left:14px;margin-bottom:4px}
  .intro li::before{content:"•";position:absolute;left:0;top:0}
  .bubble{position:absolute;text-align:center;font-size:15.5px;line-height:20px;font-weight:500;white-space:nowrap}
  .bubble h2{font-weight:300;font-size:25px;line-height:30px;margin-bottom:6px}
  .bubble p{margin-bottom:13px}
  .bubble--kid{left:451px;top:110px;width:300px}
  .bubble--school{left:110px;top:438px;width:310px}
  .bubble--school p{margin-bottom:10px}
  .bubble--teacher{left:124px;top:624px;width:300px}
  .bubble--parent{left:838px;top:540px;width:280px}
  .node{position:absolute;font-size:15px;text-align:center;line-height:19px;white-space:nowrap}
  .node--kid{left:562px;top:342px;width:80px}
  .node--school{left:394px;top:571px;width:120px}
  .node--parent{left:726px;top:581px;width:90px}
  .title{position:absolute;left:457px;top:488px;width:300px;text-align:center;color:var(--title);
    font-weight:700;font-size:28px;line-height:30px;white-space:nowrap}
</style>
</head>
<body>
<main class="flyer">
  <div class="panel"></div>
  <div class="photo" role="img" aria-label="Photo : un père et une mère accompagnent leurs deux enfants dans un couloir d'école"></div>

  <svg class="diagram" viewBox="0 0 1200 848" aria-hidden="true">
    <ellipse cx="601" cy="198" rx="168" ry="123" fill="var(--kid-orange)" opacity=".9"/>
    <ellipse cx="265" cy="507" rx="180" ry="100" fill="var(--school-green)" opacity=".9"/>
    <ellipse cx="274" cy="683" rx="180" ry="100" fill="var(--teacher-orange)" opacity=".85"/>
    <ellipse cx="978" cy="647" rx="164" ry="137" fill="var(--parent-lilac)" opacity=".9"/>
    <ellipse cx="602" cy="352" rx="75" ry="43" fill="var(--node-red)" opacity=".9"/>
    <ellipse cx="454" cy="590" rx="73" ry="48" fill="var(--node-orange)" opacity=".92"/>
    <ellipse cx="770" cy="590" rx="75" ry="47" fill="var(--node-red)" opacity=".92"/>
    <g stroke="var(--chalk)" stroke-width="4" stroke-linecap="round" fill="none" opacity=".9">
      <path d="M550 373 L414 555"/>
      <path d="M645 355 L795 550"/>
      <path d="M491 619 L755 605"/>
    </g>
  </svg>

  <div class="kid kid--left" role="img" aria-label="Dessin d'enfant : garçon au chandail vert"></div>
  <div class="kid kid--flower" role="img" aria-label="Dessin d'enfant : fillette tenant une fleur rouge"></div>
  <div class="kid kid--red" role="img" aria-label="Dessin d'enfant : fillette aux cheveux roux en robe rouge"></div>
  <div class="kid kid--right" role="img" aria-label="Dessin d'enfant : garçon au chandail bleu"></div>

  <section class="intro">
    <p class="lead">Vous serez invités, à divers moments de l’année<br>scolaire, à participer au quotidien de votre<br>enfant, par exemple . . .</p>
    <ul>
      <li>lors d’activités spéciales en classe (ex.: lecture,<br>bricolage, présentation de métiers, etc.)</li>
      <li>lors d’événements (ex.: la rentrée,<br>chorale de Noël, fête foraine, etc.)</li>
      <li>lors de sorties éducatives et sportives<br>(ex: patinage, bibliothèque, cinéma, etc.)</li>
    </ul>
    <p>De plus, vous aurez l’opportunité de venir passer<br>une période dans la classe de votre enfant.<br>Vous aurez ainsi le privilège de l’accompagner<br>lors d’un moment d’apprentissage habituel.</p>
  </section>

  <section class="bubble bubble--kid">
    <h2>Pour l’enfant :</h2>
    <p>Être fier de partager un moment<br>de sa vie scolaire, en toute<br>simplicité, avec son parent.</p>
    <p>Développer son plein potentiel.</p>
    <p>Favoriser sa réussite<br>éducative.</p>
  </section>

  <section class="bubble bubble--school">
    <h2>Pour l’école :</h2>
    <p>Vivre un projet rassembleur.</p>
    <p>Valoriser le travail de l’équipe- école.</p>
    <p>Rayonner dans sa communauté.</p>
  </section>

  <section class="bubble bubble--teacher">
    <h2>Pour l’enseignant :</h2>
    <p>Encourager la réussite de ses élèves.</p>
    <p>Multiplier les moments privilégiés<br>parent-enfant-enseignant<br>dans le milieu scolaire.</p>
  </section>

  <section class="bubble bubble--parent">
    <h2>Pour le parent</h2>
    <p>Développer un sentiment<br>d’appartenance envers l’école.</p>
    <p>Découvrir son enfant<br>en tant qu’élève.</p>
    <p>Participer à la réussite<br>et à la persévérance<br>scolaire de son enfant.</p>
  </section>

  <div class="node node--kid">Enfant</div>
  <div class="node node--school">École<br>Enseignant(e)s</div>
  <div class="node node--parent">Parent</div>

  <h1 class="title">Les journées<br>de la famille<br>de Mont-Clairval</h1>
</main>
</body>
</html>
```